Website for PeakWave Functional Training

We would like to launch a website for our boutique gym, PeakWave Functional Training. We'd like the website to have a lot of lime green which is one of our colors in our logo. The website will have a description of our workouts, membership, free trial class and location information.

Target Market(s)

Fitness enthusiasts, health conscious people, target ages 20-65, people looking to get fit and healthy, people looking to lose weight

Industry/Entity Type

Gym

Coding

Coded - Design and coding required

Number of Pages Required

1 page

Font styles to use
Serif

Colors
9ccb3b
34a7d8

Requirements
Must have
• A lot of lime green to match our logo. Let the website be fun, eye catchy. Our phone number which is 555-014-7391 to be easily dialed directly from our website.
Nice to have
• We would like to include this verbiage:
• -The Most FUN 1 hour workout
• -Affordable personal training/group training
• -Individualized workout programs
• -FUN workouts delivering results
• -Turn ON fat burn-The Most FUN 1 hour workout
• -Turn ON fat burning "EPOC" after burn
• We want our website to be easily seen on smart phones, iPads, Androids
Should not have
• Font that is hard on the eyes

```html
<!DOCTYPE html>
<html lang="en">
<head>
<meta charset="utf-8">
<title>PeakWave Functional Training</title>
<link rel="stylesheet" href="https://fonts.googleapis.com/css2?family=Lato:wght@300;400;700;900&display=swap">
<style>
:root{
  --lime:#9ccb3b;
  --blue:#34a7d8;
  --teal:#2fb0b8;
  --ink:#333333;
  --muted:#8a8a8a;
  --light:#f2f2f2;
  --dark:#3f3f3f;
  --darker:#2e2e2e;
  --footer:#4a4a4a;
  --footer-bar:#3a3a3a;
  --white:#ffffff;
}
*{box-sizing:border-box;margin:0;padding:0}
html,body{width:1200px;height:3644px;overflow:hidden}
body{font-family:'Lato',sans-serif;color:var(--ink);background:var(--white);position:relative}
a{color:inherit;text-decoration:none}
.abs{position:absolute}

/* header */
.site-header{position:absolute;top:0;left:0;width:1200px;height:97px;background:var(--white);border-bottom:1px solid #e6e6e6}
.top-strip{position:absolute;top:0;right:0;width:470px;height:24px;background:var(--lime);clip-path:polygon(14px 0,100% 0,100% 100%,0 100%);color:var(--white);font-size:14px;font-weight:700;display:flex;align-items:center;justify-content:flex-end;gap:14px;padding-right:28px}
.brand{position:absolute;left:155px;top:26px;display:flex;align-items:center;gap:10px}
.brand-dot{width:34px;height:34px;border-radius:50%;background:var(--lime)}
.brand-name{font-size:26px;font-weight:900;color:var(--lime);line-height:1}
.brand-sub{font-size:13px;font-weight:700;color:var(--lime);letter-spacing:.5px}
.main-nav{position:absolute;left:390px;top:58px;display:flex;gap:30px;font-size:12px;color:#555}
.main-nav .active{color:var(--lime);font-weight:700;border-bottom:2px solid var(--lime);padding-bottom:4px}
.social{display:flex;gap:6px}
.social span{width:16px;height:16px;border-radius:50%;background:#9a9a9a;display:block}
.header-social{position:absolute;left:965px;top:56px}

/* hero */
.hero{position:absolute;top:97px;left:0;width:1200px;height:438px;background:radial-gradient(ellipse 420px 320px at 78% 45%,#6a7178 0%,rgba(90,97,104,0) 100%),linear-gradient(100deg,#1e2326 0%,#3a4046 40%,#5c636a 70%,#2a2f33 100%)}
.hero-copy{position:absolute;left:155px;top:116px;color:var(--white)}
.hero-copy .we{font-size:28px;font-weight:300}
.hero-copy h1{font-size:18px;font-weight:900;letter-spacing:.5px;margin-top:2px}
.hero-copy p{font-size:15px;font-weight:700;line-height:21px;margin-top:24px}
.btn{display:inline-block;font-size:11px;font-weight:700;padding:0 16px;line-height:30px}
.btn-lime{background:var(--lime);color:var(--white)}
.btn-dark{background:var(--dark);color:var(--white)}
.hero .btn{position:absolute;left:155px;top:284px;line-height:32px}
.arrows{display:flex;gap:18px}
.arrow{width:24px;height:24px}
.hero-arrows{position:absolute;left:975px;top:290px}

/* about */
.about{position:absolute;top:535px;left:0;width:1200px;height:298px;background:var(--light);text-align:center}
.about .eyebrow{margin-top:43px}
.eyebrow{font-size:13px;color:#555}
.about .brand-text{font-size:26px;font-weight:900;color:var(--lime);margin-top:6px;line-height:1}
.about .brand-text small{display:block;font-size:13px;font-weight:700}
.about p{width:520px;margin:16px auto 0;font-size:10px;line-height:15px;color:var(--muted)}
.about .btn{margin-top:18px}

/* section headings */
.section-head{position:absolute;left:0;width:1200px;text-align:center}
.section-head h2{font-size:24px;font-weight:400;color:var(--ink);letter-spacing:.5px;margin-top:4px}
.section-head h2 b{color:var(--teal);font-weight:400}
.divider{display:block;margin:6px auto 0}
.section-arrows{position:absolute;left:975px}

/* programs */
.program-card{position:absolute;top:984px;width:433px;height:221px;display:flex}
.program-info{width:216px;height:100%;padding:34px 22px 0;color:var(--white);text-align:center}
.program-info h3{font-size:14px;font-weight:700}
.program-info p{font-size:10px;line-height:13px;margin-top:18px}
.program-info .btn{margin-top:14px;border:1px solid var(--white);line-height:24px;background:var(--white);color:var(--ink)}
.program-info.dark .btn{background:transparent;color:var(--white)}
.program-photo{flex:1;height:100%}

/* exercise */
.feature{position:absolute;top:1352px;width:260px;text-align:center}
.feature-circle{width:138px;height:138px;border-radius:50%;margin:0 auto;display:flex;align-items:center;justify-content:center;background:#f0f0f0}
.feature-circle.on{background:var(--lime);box-shadow:0 0 0 8px #eef6dd}
.feature h3{font-size:18px;font-weight:400;margin-top:26px}
.feature p{font-size:10px;line-height:13px;color:var(--muted);margin-top:10px;padding:0 20px}
.feature .btn{margin-top:14px;line-height:28px}

/* gallery */
.gallery{position:absolute;top:1676px;left:0;width:1200px;height:486px;background:radial-gradient(ellipse 360px 260px at 70% 30%,#6b6e72 0%,rgba(85,88,92,0) 100%),linear-gradient(90deg,#2b2d30,#55585c 50%,#2b2d30)}
.gallery .section-head h2{color:var(--white);font-weight:700}
.gallery .eyebrow{color:#ddd}
.tile{position:absolute;top:146px;width:236px;height:231px}
.tile.highlight{background:var(--lime);color:var(--white);font-size:13px;text-align:center;padding-top:90px;line-height:18px}
.gallery .view-more{position:absolute;left:558px;top:413px;background:#333;color:var(--white);line-height:30px;padding:0 18px}

/* trainers */
.trainer{position:absolute;top:2311px;width:129px;text-align:center}
.trainer-photo{width:129px;height:126px}
.trainer h4{font-size:12px;font-weight:400;margin-top:18px}
.trainer span{font-size:9px;color:var(--muted)}
.trainer .rule{height:3px;background:#cfd6dc;margin-top:8px}
.trainer .rule.on{background:var(--blue)}

/* testimonial */
.testimonial{position:absolute;top:2543px;left:0;width:1200px;height:336px;background:radial-gradient(ellipse 380px 240px at 72% 60%,#5b5e62 0%,rgba(74,77,81,0) 100%),linear-gradient(90deg,#1f2124,#4a4d51 50%,#232528)}
.testimonial .section-head h2{color:var(--white);font-weight:700}
.testimonial .eyebrow{color:#ddd}
.quote{position:absolute;top:130px;left:235px;width:730px;text-align:center;color:var(--white);font-size:13px;font-style:italic;line-height:19px;font-weight:700}
.avatar{position:absolute;left:568px;top:180px;width:60px;height:60px;border-radius:50%;background:var(--white);border:3px solid var(--white)}
.avatar i{display:block;width:100%;height:100%;border-radius:50%;background:linear-gradient(#9bb5c9,#6f8aa0)}
.t-name{position:absolute;top:251px;left:0;width:1200px;text-align:center;color:var(--white);font-size:13px}
.t-name small{display:block;font-size:10px;color:#ccc;margin-top:3px}

/* blog */
.post{position:absolute;top:3025px;width:433px}
.post-photo{width:433px;height:207px}
.post-date{position:absolute;left:15px;top:194px;width:54px;height:74px;background:var(--dark);color:var(--white);text-align:center;padding-top:14px;font-weight:900;font-size:18px;border-top:4px solid var(--lime)}
.post-date small{display:block;font-size:10px;font-weight:400;margin-top:4px}
.post h4{position:absolute;left:82px;top:216px;font-size:13px;font-weight:400;white-space:nowrap}
.post h4.on{color:var(--lime)}
.post-meta{position:absolute;left:82px;top:244px;font-size:9px;color:var(--muted);display:flex;gap:18px;white-space:nowrap}

/* footer */
.site-footer{position:absolute;top:3333px;left:0;width:1200px;height:262px;background:var(--footer);color:#ddd}
.foot-col{position:absolute;top:46px}
.foot-col h5{font-size:16px;font-weight:400;color:var(--white)}
.foot-links{list-style:none;margin-top:16px;font-size:11px;line-height:19px}
.foot-links li:before{content:"› ";color:#bbb}
.foot-links li.on{color:var(--lime)}
.foot-col p{font-size:10px;line-height:14px;margin-top:16px;color:#ccc}
.field{width:230px;border-bottom:1px solid #888;font-size:10px;padding:14px 0 8px;color:#bbb}
.foot-col .btn{margin-top:20px;line-height:26px;padding:0 26px}
.phone{font-size:20px;color:var(--white);margin-top:12px;display:block}
.email{font-size:10px;color:#ccc}
.footer-social{margin-top:12px}
.footer-social span{background:#d8d8d8}
.foot-bar{position:absolute;top:3595px;left:0;width:1200px;height:49px;background:var(--footer-bar);color:#aaa;font-size:10px;padding:19px 0 0 155px}
.to-top{position:absolute;left:1025px;top:14px;width:20px;height:20px;border-radius:50%;background:var(--lime)}
</style>
</head>
<body>

<header class="site-header">
  <div class="top-strip"><a href="tel:5550147391">555-014-7391</a><span>/</span><span>We are open 24/7</span></div>
  <div class="brand">
    <span class="brand-dot"></span>
    <div><div class="brand-name">PEAKWAVE</div><div class="brand-sub">Functional Training</div></div>
  </div>
  <nav class="main-nav">
    <a class="active">Home</a><a>About Us</a><a>Exercise &amp; Trainings</a><a>Programs</a><a>Gallery</a><a>Blog</a><a>Contact Us</a>
  </nav>
  <div class="social header-social"><span></span><span></span><span></span><span></span></div>
</header>

<section class="hero" role="img" aria-label="Athlete training hard on a rowing machine in the gym">
  <div class="hero-copy">
    <div class="we">We are</div>
    <h1>PEAKWAVE FUNCTIONAL TRAINING</h1>
    <p>The best fitness centre.<br>You will always look sharp and utilize 100% of your body<br>for modernization.</p>
  </div>
  <a class="btn btn-lime">Start Free Trial Class</a>
  <div class="arrows hero-arrows">
    <svg class="arrow" viewBox="0 0 24 24"><path d="M20 12H4M10 6l-6 6 6 6" fill="none" stroke="#fff" stroke-width="2"/></svg>
    <svg class="arrow" viewBox="0 0 24 24"><path d="M4 12h16M14 6l6 6-6 6" fill="none" stroke="#9ccb3b" stroke-width="2"/></svg>
  </div>
</section>

<section class="about">
  <div class="eyebrow">Discover about us</div>
  <div class="brand-text">PEAKWAVE<small>Functional Training</small></div>
  <p>Lorem Ipsum is simply dummy text of the printing and typesetting industry. Lorem Ipsum has been the industry's standard dummy text ever since the 1500s, when an unknown printer took a galley of type and scrambled it to make a type specimen book. It has survived not only five centuries, but also the leap into electronic typesetting, remaining essentially unchanged ...</p>
  <a class="btn btn-dark">Read More</a>
</section>

<svg width="0" height="0" style="position:absolute">
  <defs>
    <g id="divider"><path d="M0 5h18M44 5h18" stroke="#9ccb3b" stroke-width="2"/><path d="M26 1v8M22 5h8M36 1v8M32 5h8" stroke="#9ccb3b" stroke-width="2"/></g>
    <g id="arrow-pair"><path d="M22 12H4M10 6l-6 6 6 6" fill="none" stroke="#bbb" stroke-width="2"/><path d="M44 12h18M56 6l6 6-6 6" fill="none" stroke="#9ccb3b" stroke-width="2"/></g>
  </defs>
</svg>

<div class="section-head" style="top:876px">
  <div class="eyebrow">Functional Training</div>
  <h2><b>OUR</b> PROGRAMS</h2>
  <svg class="divider" width="62" height="10"><use href="#divider"/></svg>
</div>
<svg class="section-arrows" style="top:890px" width="66" height="24"><use href="#arrow-pair"/></svg>

<article class="program-card" style="left:155px">
  <div class="program-info" style="background:var(--lime)">
    <h3>High Kick Class</h3>
    <p>There are many variations of passages of Lorem Ipsum available, but the majority have suffered alteration.</p>
    <a class="btn">Get Membership</a>
  </div>
  <div class="program-photo" role="img" aria-label="Woman throwing a high kick at a punching bag" style="background:radial-gradient(ellipse 90px 120px at 35% 50%,#8a7566 0%,rgba(138,117,102,0) 100%),linear-gradient(135deg,#2f2f2f,#6e6e6e)"></div>
</article>
<article class="program-card" style="left:612px">
  <div class="program-info dark" style="background:#555">
    <h3>Relaxing Yoga</h3>
    <p>There are many variations of passages of Lorem Ipsum available, but the majority have suffered alteration.</p>
    <a class="btn">Get Membership</a>
  </div>
  <div class="program-photo" role="img" aria-label="Yoga class seated in meditation poses" style="background:linear-gradient(180deg,#ece8e4 0%,#d9cfcc 60%,#4a5a8a 100%)"></div>
</article>

<div class="section-head" style="top:1236px">
  <div class="eyebrow">Why Choose Us?</div>
  <h2><b>EXERCISE</b> &amp; TRAINING</h2>
  <svg class="divider" width="62" height="10"><use href="#divider"/></svg>
</div>

<div class="feature" style="left:166px">
  <div class="feature-circle on">
    <svg width="50" height="40" viewBox="0 0 50 40"><path d="M6 14v12M12 10v20M38 10v20M44 14v12M12 20h26" stroke="#fff" stroke-width="5" fill="none"/></svg>
  </div>
  <h3>Exercise</h3>
  <p>Lorem ipsum dolor sit amet, consectetur adipiscing elit. Suspendisse feugiat non eros vel ultricies. Phasellus ultricies tempus ...</p>
  <a class="btn btn-lime">Read More</a>
</div>
<div class="feature" style="left:468px">
  <div class="feature-circle">
    <svg width="44" height="44" viewBox="0 0 44 44"><circle cx="22" cy="8" r="5" fill="#2fb0b8"/><path d="M8 18h28M22 18v12M16 40l6-10 6 10" stroke="#2fb0b8" stroke-width="4" fill="none"/></svg>
  </div>
  <h3>Personal Training</h3>
  <p>Lorem ipsum dolor sit amet, consectetur adipiscing elit. Suspendisse feugiat non eros vel ultricies. Phasellus ultricies tempus ...</p>
  <a class="btn btn-dark">Read More</a>
</div>
<div class="feature" style="left:774px">
  <div class="feature-circle">
    <svg width="48" height="44" viewBox="0 0 48 44"><circle cx="16" cy="8" r="5" fill="#2fb0b8"/><circle cx="32" cy="8" r="5" fill="#2fb0b8"/><path d="M16 16v14M32 16v14M10 40l6-10 6 10M26 40l6-10 6 10" stroke="#2fb0b8" stroke-width="4" fill="none"/></svg>
  </div>
  <h3>Group Training</h3>
  <p>Lorem ipsum dolor sit amet, consectetur adipiscing elit. Suspendisse feugiat non eros vel ultricies. Phasellus ultricies tempus ...</p>
  <a class="btn btn-dark">Read More</a>
</div>

<section class="gallery" role="img" aria-label="Dimmed photo of a woman working out in the gym">
  <div class="section-head" style="top:44px">
    <div class="eyebrow">Watch Us?</div>
    <h2>PHOTO GALLERY</h2>
    <svg class="divider" width="62" height="10"><use href="#divider"/></svg>
  </div>
  <svg class="section-arrows" style="top:66px" width="66" height="24"><use href="#arrow-pair"/></svg>
  <div class="tile" style="left:0;background:linear-gradient(160deg,#e8e6e3 0%,#9a8a80 45%,#3a3a3a 100%)" role="img" aria-label="Partner dumbbell training"></div>
  <div class="tile highlight" style="left:241px">Affordable<br>personal training</div>
  <div class="tile" style="left:482px;background:linear-gradient(160deg,#6a6d76 0%,#c7b2a4 50%,#2f4478 100%)" role="img" aria-label="Woman doing sit-ups"></div>
  <div class="tile" style="left:723px;background:radial-gradient(circle at 55% 45%,#f0f0f0 0%,#a8a8a8 45%,#4e4e4e 100%)" role="img" aria-label="Close-up of dumbbells on a rack"></div>
  <div class="tile" style="left:964px;background:linear-gradient(180deg,#ddd4cf 0%,#c79c8f 50%,#3b5fa0 100%)" role="img" aria-label="Women stretching on yoga mats"></div>
  <a class="btn view-more">View More</a>
</section>

<div class="section-head" style="top:2216px">
  <div class="eyebrow">Expert Team</div>
  <h2><b>MEET OUR</b> TRAINERS</h2>
  <svg class="divider" width="62" height="10"><use href="#divider"/></svg>
</div>
<svg class="abs" style="left:255px;top:2388px" width="24" height="24" viewBox="0 0 24 24"><path d="M20 12H4M10 6l-6 6 6 6" fill="none" stroke="#bbb" stroke-width="2"/></svg>
<svg class="abs" style="left:916px;top:2388px" width="24" height="24" viewBox="0 0 24 24"><path d="M4 12h16M14 6l6 6-6 6" fill="none" stroke="#9ccb3b" stroke-width="2"/></svg>

<div class="trainer" style="left:308px">
  <div class="trainer-photo" role="img" aria-label="Portrait of a male personal trainer" style="background:linear-gradient(#e4e4e4,#6a6a6a 60%,#2a2a2a)"></div>
  <h4>Marco Lintel</h4><span>Personal Trainer</span><div class="rule"></div>
</div>
<div class="trainer" style="left:462px">
  <div class="trainer-photo" role="img" aria-label="Portrait of a female group trainer" style="background:var(--lime)"></div>
  <h4>Dana Fairlow</h4><span>Group Trainer</span><div class="rule on"></div>
</div>
<div class="trainer" style="left:612px">
  <div class="trainer-photo" role="img" aria-label="Portrait of a male group trainer" style="background:linear-gradient(#a9c9e6,#c49a7e 55%,#2f5d92)"></div>
  <h4>Theo Ransom</h4><span>Group Trainer</span><div class="rule"></div>
</div>
<div class="trainer" style="left:763px">
  <div class="trainer-photo" role="img" aria-label="Portrait of a female personal trainer" style="background:linear-gradient(#a3553f,#6e4a3e 50%,#2f2f2f)"></div>
  <h4>Priya Valdes</h4><span>Personal Trainer</span><div class="rule"></div>
</div>

<section class="testimonial" role="img" aria-label="Dimmed photo of a woman exercising">
  <div class="section-head" style="top:44px">
    <div class="eyebrow">Testimonial</div>
    <h2>WHY PEOPLE LOVE US?</h2>
    <svg class="divider" width="62" height="10"><use href="#divider"/></svg>
  </div>
  <p class="quote">Lorem ipsum dolor sit amet, consectetur adipiscing elit. Suspendisse feugiat non eros vel ultricies. Phasellus ultricies tempus risus a tristique. Interdum et malesuada fames ac ante ipsum primis in faucibus. Sed sed blandit arcu.</p>
  <svg class="abs" style="left:523px;top:198px" width="24" height="24" viewBox="0 0 24 24"><path d="M20 12H4M10 6l-6 6 6 6" fill="none" stroke="#fff" stroke-width="2"/></svg>
  <div class="avatar" role="img" aria-label="Member portrait"><i></i></div>
  <svg class="abs" style="left:649px;top:198px" width="24" height="24" viewBox="0 0 24 24"><path d="M4 12h16M14 6l6 6-6 6" fill="none" stroke="#9ccb3b" stroke-width="2"/></svg>
  <div class="t-name">Mrs. Ellen Marsh<small>Member since 2015</small></div>
</section>

<div class="section-head" style="top:2912px">
  <div class="eyebrow">Daily Updates</div>
  <h2><b>LATEST</b> BLOG</h2>
  <svg class="divider" width="62" height="10"><use href="#divider"/></svg>
</div>
<svg class="section-arrows" style="top:2944px" width="66" height="24"><use href="#arrow-pair"/></svg>

<article class="post" style="left:155px">
  <div class="post-photo" role="img" aria-label="Couple lifting a barbell together" style="background:linear-gradient(110deg,#3e3e3e 0%,#8a8a8a 30%,#e2b89c 55%,#c0302c 85%,#8d1f1f 100%)"></div>
  <div class="post-date">28<small>Dec.</small></div>
  <h4>Lorem ipsum dolor sit amet</h4>
  <div class="post-meta"><span>Standard Chunk</span><span>Sport and Fitness</span><span>♥ 56</span><span>07</span></div>
</article>
<article class="post" style="left:612px">
  <div class="post-photo" role="img" aria-label="Group doing lunges in a fitness class" style="background:linear-gradient(180deg,#e6e4e2 0%,#c9b7b2 45%,#b1425a 75%,#3c3c3c 100%)"></div>
  <div class="post-date">06<small>Jan.</small></div>
  <h4 class="on">Lorem ipsum dolor sit amet</h4>
  <div class="post-meta"><span>Standard Chunk</span><span>Sport and Fitness</span><span>♥ 54</span><span>07</span></div>
</article>

<footer class="site-footer">
  <div class="foot-col" style="left:155px">
    <h5>PeakWave Functional Training.</h5>
    <ul class="foot-links">
      <li class="on">Home</li><li>About Us</li><li>Exercise &amp; Trainings</li><li>Programs</li><li>Gallery</li><li>Blog</li><li>Contact Us</li>
    </ul>
  </div>
  <div class="foot-col" style="left:462px">
    <h5>Our Newsletter</h5>
    <p>Be the first to receive exciting news, features &amp;<br>special offers.</p>
    <div class="field">Enter your email...</div>
    <a class="btn btn-lime">Subscribe</a>
  </div>
  <div class="foot-col" style="left:797px">
    <h5>Contact Us</h5>
    <p>220 Harbor Lane, Suite 4B<br>Brookfield 48201</p>
    <a class="phone" href="tel:5550147391">555-014-7391</a>
    <div class="email">hello@peakwavefit.com</div>
    <div class="social footer-social"><span></span><span></span><span></span><span></span></div>
  </div>
</footer>
<div class="foot-bar">© 2017 PeakWave Functional Training . All Rights Reserved.
  <span class="to-top"><svg width="20" height="20" viewBox="0 0 20 20"><path d="M10 14V6M6 10l4-4 4 4" fill="none" stroke="#fff" stroke-width="2"/></svg></span>
</div>

</body>
</html>
```